NEW YORK Plumbing/utility company 10 year anniversary business card

Looking For simple back and front business card would like to include a few things in description
We offer 24/7 emergency service
residential
commercial
industrial
municipal
services offered
Plumbing
hydro excavation
hydro jetting
Well pumps
Sewer pumps
water mains
sewer mains

```html
<!DOCTYPE html>
<html lang="en">
<head>
<meta charset="utf-8">
<title>Kestrel Creek Water &amp; Sewer – Business Card</title>
<link rel="stylesheet" href="https://fonts.googleapis.com/css2?family=Roboto:wght@400;500;700&display=swap">
<style>
  :root {
    --backdrop: #e3e3e3;
    --brand-blue: #1c5f9b;
    --accent-blue: #33a6de;
    --card-white: #f4f4f4;
    --ink: #2f2f2f;
    --on-dark: #ffffff;
  }
  * { box-sizing: border-box; margin: 0; padding: 0; }
  html, body { width: 1200px; height: 960px; overflow: hidden; }
  body {
    background: var(--backdrop);
    font-family: "Roboto", Arial, sans-serif;
    position: relative;
  }
  .card {
    position: absolute;
    left: 297px;
    width: 610px;
    height: 349px;
    overflow: hidden;
  }

  /* Front */
  .card-front { top: 111px; background: var(--brand-blue); color: var(--on-dark); }
  .front-brand {
    position: absolute; left: 40px; top: 108px; width: 316px;
    text-align: center;
  }
  .brand-name {
    font-weight: 700; font-size: 24px; line-height: 30px; letter-spacing: 1.5px;
  }
  .front-brand .brand-name { color: var(--on-dark); }
  .tagline { margin-top: 12px; font-weight: 500; font-size: 15px; }
  .divider {
    position: absolute; left: 344px; top: 82px; width: 2px; height: 178px;
    background: var(--on-dark);
  }
  .services { position: absolute; left: 370px; top: 86px; }
  .services-title { font-weight: 500; font-size: 16px; margin-bottom: 5px; }
  .services-list { list-style: none; }
  .services-list li {
    display: flex; align-items: center; gap: 4px;
    font-size: 16px; line-height: 20.3px;
  }
  .drop { width: 9px; height: 12px; fill: var(--accent-blue); flex: none; }
  .sectors {
    position: absolute; left: 0; right: 0; top: 305px;
    display: flex; justify-content: center; align-items: center; gap: 4px;
    font-size: 15px; letter-spacing: 0.2px;
  }

  /* Back */
  .card-back { top: 513px; background: var(--card-white); }
  .side-band { position: absolute; left: 0; top: 0; width: 40px; height: 349px; }
  .back-brand { position: absolute; left: 50px; top: 58px; }
  .back-brand .brand-name { color: var(--brand-blue); font-size: 26px; line-height: 34px; }
  .address {
    position: absolute; left: 50px; top: 205px;
    font-size: 16px; line-height: 20.5px; color: var(--ink);
  }
  .contacts { position: absolute; left: 50px; top: 252px; list-style: none; }
  .contacts li {
    display: flex; align-items: center; gap: 5px;
    font-size: 16px; line-height: 20.5px; color: var(--ink);
  }
  .contact-icon { width: 14px; height: 14px; fill: none; stroke: var(--accent-blue); stroke-width: 1.6; }
  .person { position: absolute; right: 40px; top: 60px; text-align: right; }
  .person-name { font-weight: 500; font-size: 20px; color: var(--brand-blue); }
  .person-role { font-size: 15px; color: var(--accent-blue); margin-top: 2px; }
</style>
</head>
<body>

<svg width="0" height="0" style="position:absolute">
  <symbol id="drop-shape" viewBox="0 0 10 13">
    <path d="M5 0 C6.5 3 10 6 10 8.5 A5 4.6 0 0 1 0 8.5 C0 6 3.5 3 5 0 Z"/>
  </symbol>
</svg>

<section class="card card-front">
  <div class="front-brand">
    <div class="brand-name">KESTREL CREEK<br>WATER &amp; SEWER</div>
    <div class="tagline">24/7 Emergency Service</div>
  </div>
  <div class="divider"></div>
  <div class="services">
    <h2 class="services-title">Services Offered</h2>
    <ul class="services-list">
      <li><svg class="drop"><use href="#drop-shape"/></svg>Plumbing</li>
      <li><svg class="drop"><use href="#drop-shape"/></svg>Hydro Excavation</li>
      <li><svg class="drop"><use href="#drop-shape"/></svg>Hydro Jetting</li>
      <li><svg class="drop"><use href="#drop-shape"/></svg>Well Pumps</li>
      <li><svg class="drop"><use href="#drop-shape"/></svg>Sewer Pumps</li>
      <li><svg class="drop"><use href="#drop-shape"/></svg>Water Mains</li>
      <li><svg class="drop"><use href="#drop-shape"/></svg>Sewer Mains</li>
    </ul>
  </div>
  <div class="sectors">
    <span>RESIDENTIAL</span><svg class="drop"><use href="#drop-shape"/></svg>
    <span>COMMERCIAL</span><svg class="drop"><use href="#drop-shape"/></svg>
    <span>INDUSTRIAL</span><svg class="drop"><use href="#drop-shape"/></svg>
    <span>MUNICIPAL</span>
  </div>
</section>

<section class="card card-back">
  <svg class="side-band" viewBox="0 0 40 349">
    <polygon points="0,0 19,0 19,349 0,349" fill="var(--accent-blue)"/>
    <polygon points="0,0 19,0 19,192 0,176" fill="var(--brand-blue)"/>
  </svg>
  <div class="back-brand">
    <div class="brand-name">KESTREL CREEK<br>WATER &amp; SEWER</div>
  </div>
  <div class="person">
    <div class="person-name">Daniel Brooks</div>
    <div class="person-role">Founder / Owner</div>
  </div>
  <p class="address">14 Alder Ridge Road<br>Millbrook Falls, NY 12000</p>
  <ul class="contacts">
    <li>
      <svg class="contact-icon" viewBox="0 0 14 14"><path d="M3 1.5 L5 1.5 L6 4.5 L4.5 5.5 A7 7 0 0 0 8.5 9.5 L9.5 8 L12.5 9 L12.5 11 A1.5 1.5 0 0 1 11 12.5 A9.5 9.5 0 0 1 1.5 3 A1.5 1.5 0 0 1 3 1.5 Z"/></svg>
      845-555-0142
    </li>
    <li>
      <svg class="contact-icon" viewBox="0 0 14 14"><rect x="1.5" y="3" width="11" height="8"/><path d="M1.5 3 L7 7.5 L12.5 3"/></svg>
      daniel@kestrelcreek.com
    </li>
    <li>
      <svg class="contact-icon" viewBox="0 0 14 14"><circle cx="7" cy="7" r="5.5"/><ellipse cx="7" cy="7" rx="2.3" ry="5.5"/><path d="M1.5 7 H12.5"/></svg>
      www.kestrelcreek.com
    </li>
  </ul>
</section>

</body>
</html>
```